Business Card Layout and Stationary Layout
Business Card Layout and Stationary Layout -
Creative Brief
Use same font as used in my logo
CHANGE THE FONT TO SOMETHING NEW
Professional
Paul Dawson
P.O. Box 31842 Seattle WA 98173
Paul@Brintacor.com
Brintacor.com
We need a new font. Something where we can have BRINTACOR used just in font form. We love our logo, but we want a more creative high-powered, stand-alone font. We also need a letterhead layout and an invoice layout. Will pay winner an extra $50 for these two items.

```html
<!DOCTYPE html>
<html lang="en">
<head>
<meta charset="utf-8">
<title>Brintacor Business Card</title>
<link href="https://fonts.googleapis.com/css2?family=PT+Sans:wght@400;700&display=swap" rel="stylesheet">
<style>
  :root {
    --page-bg: #e9e6e1;
    --card-white: #ffffff;
    --brand-green: #2f8f2a;
    --green-light: #4aa83a;
    --green-dark: #1c6b1c;
    --swoosh-grey: #c9cbcc;
    --text-white: #ffffff;
    --card-shadow: rgba(0, 0, 0, 0.22);
  }
  * { margin: 0; padding: 0; box-sizing: border-box; }
  html, body {
    width: 1200px;
    height: 780px;
    overflow: hidden;
    background: var(--page-bg);
    font-family: "PT Sans", sans-serif;
  }
  .business-card {
    position: absolute;
    left: 100px;
    top: 105px;
    width: 1000px;
    height: 570px;
    border-radius: 30px;
    overflow: hidden;
    background: var(--card-white);
    box-shadow: 0 10px 30px var(--card-shadow);
  }
  .card-shapes {
    position: absolute;
    inset: 0;
  }
  .brand-mark {
    position: absolute;
    left: 0;
    right: 0;
    top: 70px;
    display: flex;
    flex-direction: column;
    align-items: center;
  }
  .brand-dot {
    width: 140px;
    height: 140px;
    border-radius: 50%;
    background: var(--brand-green);
  }
  .brand-name {
    margin-top: 14px;
    font-size: 68px;
    font-weight: 700;
    line-height: 1;
    color: var(--brand-green);
  }
  .contact-person {
    position: absolute;
    right: 540px;
    top: 392px;
    text-align: right;
    color: var(--text-white);
  }
  .person-name {
    font-size: 34px;
    font-weight: 700;
    line-height: 1.15;
  }
  .postal-address {
    font-size: 25px;
    line-height: 1.3;
    margin-top: 4px;
  }
  .contact-divider {
    position: absolute;
    left: 488px;
    top: 385px;
    width: 2px;
    height: 125px;
    background: var(--text-white);
  }
  .contact-lines {
    position: absolute;
    left: 520px;
    top: 388px;
    list-style: none;
    color: var(--text-white);
    font-size: 25px;
  }
  .contact-lines li {
    display: flex;
    align-items: center;
    gap: 12px;
    height: 40px;
  }
  .contact-icon {
    width: 22px;
    height: 22px;
    flex: none;
  }
</style>
</head>
<body>
  <div class="business-card">
    <svg class="card-shapes" width="1000" height="570" viewBox="0 0 1000 570">
      <defs>
        <linearGradient id="greenBand" x1="0" y1="0" x2="0" y2="1">
          <stop offset="0" stop-color="var(--green-light)"/>
          <stop offset="1" stop-color="var(--green-dark)"/>
        </linearGradient>
      </defs>
      <path class="grey-swoosh" d="M0 335 C 220 300, 420 280, 620 300 C 780 315, 900 300, 1000 270 L1000 300 C 880 330, 760 340, 600 330 C 420 318, 220 335, 0 360 Z" fill="var(--swoosh-grey)"/>
      <path class="green-band" d="M0 360 C 220 335, 420 318, 600 330 C 760 340, 880 330, 1000 300 L1000 570 L0 570 Z" fill="url(#greenBand)"/>
    </svg>

    <div class="brand-mark">
      <div class="brand-dot"></div>
      <div class="brand-name">Brintacor</div>
    </div>

    <div class="contact-person">
      <div class="person-name">Paul Dawson</div>
      <div class="postal-address">P.O. Box 31842<br>Seattle WA 98173</div>
    </div>

    <div class="contact-divider"></div>

    <ul class="contact-lines">
      <li>
        <svg class="contact-icon" viewBox="0 0 22 22"><rect x="6" y="1" width="10" height="20" rx="2" fill="none" stroke="#fff" stroke-width="2"/><rect x="8" y="4" width="6" height="9" fill="#fff"/></svg>
        <span>206-555-0182</span>
      </li>
      <li>
        <svg class="contact-icon" viewBox="0 0 22 22"><rect x="1" y="5" width="20" height="13" fill="none" stroke="#fff" stroke-width="2"/><path d="M1 5 L11 13 L21 5" fill="none" stroke="#fff" stroke-width="2"/></svg>
        <span>Paul@Brintacor.com</span>
      </li>
      <li>
        <svg class="contact-icon" viewBox="0 0 22 22"><circle cx="11" cy="11" r="9" fill="#fff"/></svg>
        <span>Brintacor.com</span>
      </li>
    </ul>
  </div>
</body>
</html>
```